Import Export Business Needs a Website

We need a website design that is fluid and utilizing todays visual appeal. HTML5 Wordpress that can be fully customized after a turnkey solution by us. We need to be able to have full control of the site's backend and allow for creative content to be easily changed.

We own a template that we would like to have utilized and we already have a LOGO, we would like site content and language to be provided for us. Basic informational site, no need for shopping carts, blogs, or surveys.

We want to be as similar as possible as the appearance to https://www.brindlefloorcraft.com

These below are in our industry (We want a better website than our Competitors)
Competition:

http://www.vrolantrade.com/index.html
http://www.pemsupply.com/
http://www.orvelo-brimm-hemp.com/
http://www.lqtarrow.com/index.html
http://www.faxuline.com/index.php

Customers:
https://www.brindlefloorcraft.com/
http://www.tellumats.com/en
http://www.zbmats.com/

Supplier:
http://dovesholdings.com/
http://www.plumavex.com/
http://www.bellonweave.com/en/index.html
Updates

Project Deadline Extended
Reason: We have been extremely busy with tracking a shipment we have not had time to review the designs in depth or get with a designer to customize settings. We will be selecting someone tomorrow to work with and would like to have the weekend and the first few days of next week to discuss the site in detail.

Target Market(s)

Textile Carpet Fibers Fabric

Industry/Entity Type

Business

Number of Pages Required

5+ page

Font styles to use
Serif
Sans Serif
Other font styles liked:
• font has been uploaded for use in logo and small accents

Colors
3176b5
ffffff
85cae6
3377b5
0255a3
34a6d7
c4c4c4
c3c3c3
aaaaaa

Requirements
Must have
• Project must utilize provided template or substitute template can be provided but must be for wordpress. Fonts have been uploaded for LOGO provided.
Nice to have
• Nice to have metrics to know site visitors and demographics
Should not have
• ecommerce, shopping carts

```html
<!DOCTYPE html>
<html lang="en">
<head>
<meta charset="utf-8">
<title>Meridel International</title>
<link href="https://fonts.googleapis.com/css2?family=Open+Sans:wght@300;400;600&family=Oswald:wght@400&display=swap" rel="stylesheet">
<style>
:root{
  --blue:#3176b5;
  --blue-bright:#2f88c9;
  --blue-deep:#0255a3;
  --sky:#85cae6;
  --ink:#222;
  --text:#555;
  --grey-bg:#ececec;
  --line:#aaaaaa;
  --white:#ffffff;
  --footer:#161616;
}
*{margin:0;padding:0;box-sizing:border-box}
html,body{width:1200px;height:3442px;overflow:hidden}
body{position:relative;font-family:"Open Sans",Arial,sans-serif;color:var(--ink);background:var(--white)}
.abs{position:absolute}

/* hero */
.hero{left:0;top:0;width:1200px;height:592px;background:linear-gradient(135deg,#1c2430 0%,#3a4250 45%,#2a3340 70%,#151a22 100%)}
.hero-media{left:0;top:0;width:1200px;height:592px;background:radial-gradient(ellipse at 40% 70%,rgba(120,130,140,.35),transparent 60%)}
.brand{left:82px;top:26px;display:flex;flex-direction:column;align-items:center;color:var(--white)}
.brand-mark{width:46px;height:46px;border-radius:50%;background:var(--white);margin-bottom:8px}
.brand-name{font-size:17px;font-weight:600;letter-spacing:1px}
.menu{left:1034px;top:36px;color:var(--white);font-size:15px;display:flex;align-items:center;gap:10px}
.hero-title{left:0;width:1200px;top:244px;text-align:center;color:var(--white);font-family:"Oswald",Arial,sans-serif;font-weight:400;font-size:40px;line-height:52px;letter-spacing:.5px}
.hero-sub{left:0;width:1200px;top:306px;text-align:center;color:var(--white);font-size:25px;font-weight:300}
.slide-arrow{top:285px;width:22px;height:22px}

/* intro */
.intro-photo{left:406px;top:661px;width:204px;height:321px;background:linear-gradient(180deg,#6f8fae 0%,#2d5878 40%,#c2503a 70%,#1d3f5c 100%)}
.welcome{left:610px;top:512px;width:503px;height:608px;background:var(--blue-bright);color:var(--white);padding:70px 46px 0 46px}
.welcome h2{font-weight:400;font-size:19px;padding-bottom:10px;border-bottom:1px solid rgba(255,255,255,.7);margin-bottom:24px}
.welcome p{font-size:12px;line-height:22.5px;font-weight:300;text-align:justify}
.btn-outline{display:inline-block;margin-top:28px;border:1px solid currentColor;border-radius:18px;padding:8px 22px;font-size:11px}
.experience{left:207px;top:982px;width:509px;height:355px;background:linear-gradient(180deg,rgba(236,236,240,.96),rgba(226,226,232,.96));padding:58px 48px 0 48px;color:var(--ink)}
.experience h2{font-weight:400;font-size:24px;margin-bottom:14px}
.experience p{font-size:12px;line-height:23px;color:#444;text-align:justify}
.experience .btn-outline{color:var(--blue-deep);margin-top:24px}

/* what we do */
.section-grey{left:0;top:1243px;width:1200px;height:1134px;background:var(--grey-bg)}
.section-title{left:0;width:1200px;text-align:center;font-size:25px;font-weight:400}
.card{left:151px;width:900px;height:326px;background:var(--white);box-shadow:0 1px 3px rgba(0,0,0,.15)}
.card-body{position:absolute;top:0;padding:54px 48px 0 42px}
.card-body h3{font-weight:400;font-size:25px;margin-bottom:10px}
.card-body p{font-size:12px;line-height:21px;color:var(--text);text-align:justify}
.btn-fill{display:inline-block;margin-top:14px;background:var(--blue-bright);color:var(--white);border-radius:18px;padding:9px 22px;font-size:11px}
.card-media{position:absolute;top:0;height:326px}

/* services */
.services{left:0;top:2377px;width:1200px;height:459px;background:linear-gradient(180deg,#234f8e,#1b4078)}
.service{top:2570px;width:300px;text-align:center;color:var(--white)}
.service svg{display:block;margin:0 auto 38px}
.service h4{font-weight:400;font-size:17px;margin-bottom:6px}
.service p{font-size:12px;line-height:19px;font-weight:300;padding:0 36px}

/* contact */
.contact-field{border-bottom:1px solid #666;font-size:16px;padding-bottom:4px;color:#222}
.submit{left:537px;top:3133px;width:126px;height:34px;background:var(--blue-bright);color:var(--white);border-radius:17px;text-align:center;line-height:34px;font-size:14px}

/* footer */
.footer{left:0;top:3269px;width:1200px;height:173px;background:var(--footer);color:var(--white)}
.footer-links{left:0;width:1200px;top:44px;text-align:center;font-size:12px}
.footer-social{left:0;width:1200px;top:80px;display:flex;justify-content:center;gap:8px}
.footer-social span{width:22px;height:22px;border:1px solid #aaa;border-radius:50%}
.copyright{left:0;width:1200px;top:118px;text-align:center;font-size:11px}
</style>
</head>
<body>

<section class="abs hero">
  <div class="abs hero-media" role="img" aria-label="Business person holding a tablet with a network of connection lines"></div>
  <div class="abs brand"><span class="brand-mark"></span><span class="brand-name">MERIDEL</span></div>
  <div class="abs menu">
    <svg width="16" height="13" viewBox="0 0 16 13"><rect width="16" height="2.5" fill="#fff"/><rect y="5.2" width="16" height="2.5" fill="#fff"/><rect y="10.5" width="16" height="2.5" fill="#fff"/></svg>
    MENU
  </div>
  <h1 class="abs hero-title">MERIDEL INTERNATIONAL</h1>
  <p class="abs hero-sub">Porro quisquam est qui dolorem ipsum</p>
  <svg class="abs slide-arrow" style="left:81px" viewBox="0 0 22 22"><circle cx="11" cy="11" r="11" fill="#111"/><path d="M13 6l-5 5 5 5" stroke="#fff" stroke-width="2" fill="none"/></svg>
  <svg class="abs slide-arrow" style="left:1090px" viewBox="0 0 22 22"><circle cx="11" cy="11" r="11" fill="#111"/><path d="M9 6l5 5-5 5" stroke="#fff" stroke-width="2" fill="none"/></svg>
</section>

<div class="abs section-grey"></div>

<div class="abs intro-photo" role="img" aria-label="Aerial view of a container ship loaded with cargo at sea"></div>

<article class="abs welcome">
  <h2>WELCOME TO MERIDEL INTERNATIONAL</h2>
  <p>It has survived not only five centuries, but also the leap into electronic typesetting, remaining essentially unchanged. It was popularised in the 1960s with the release of Pressmark sheets containing Lorem Ipsum passages, and more recently with desktop publishing software like Quillset Composer including versions of Lorem Ipsum The point of using Lorem Ipsum is that it has a more-or-less normal distribution of letters, to using 'Content here, content here', making it look like readable English. Many desktop publishing packages and web page editors now use Lorem Ipsum as their default model text.</p>
  <span class="btn-outline">READ MORE</span>
</article>

<article class="abs experience">
  <h2>EXPERIENCE</h2>
  <p>It has survived not only five centuries, but also the leap into electronic typesetting, remaining essentially unchanged. It was popularised in the 1960s with the release of Pressmark sheets containing Lorem Ipsum passages, and more recently with desktop publishing software like Quillset Composer including versions of Lorem Ipsum The point of using Lorem Ipsum .</p>
  <span class="btn-outline">READ MORE</span>
</article>

<h2 class="abs section-title" style="top:1430px">WHAT WE DO</h2>

<article class="abs card" style="top:1532px">
  <div class="card-body" style="left:0;width:489px">
    <h3>EXPORT IMPORT</h3>
    <p>It has survived not only five centuries, but also the leap into electronic typesetting, remaining essentially unchanged. It was popularised in the 1960s with the release of Pressmark sheets containing Lorem Ipsum passages, and more recently with desktop publishing software like Quillset Composer including versions of Lorem Ipsum The point of using Lorem</p>
    <span class="btn-fill">READ MORE</span>
  </div>
  <div class="card-media" style="left:489px;width:411px;background:linear-gradient(160deg,#2c3f66 0%,#7a6a8a 40%,#c0392b 65%,#2a3550 100%)" role="img" aria-label="Red cargo truck on a road with a plane overhead at dusk"></div>
</article>

<article class="abs card" style="top:1893px">
  <div class="card-media" style="left:0;width:409px;background:linear-gradient(100deg,#8a7a5c 0%,#a0443a 35%,#6e2630 55%,#6b5a4a 80%,#c9a575 100%)" role="img" aria-label="Fan of textile carpet fiber samples in many colours"></div>
  <div class="card-body" style="left:409px;width:491px">
    <h3>TEXTILE CARPET FIBERS</h3>
    <p>It has survived not only five centuries, but also the leap into electronic typesetting, remaining essentially unchanged. It was popularised in the 1960s with the release of Pressmark sheets containing Lorem Ipsum passages, and more recently with desktop publishing software like Quillset Composer including versions of Lorem Ipsum The point of using Lorem</p>
    <span class="btn-fill">READ MORE</span>
  </div>
</article>

<section class="abs services" role="img" aria-label="Port cranes and shipping containers tinted blue"></section>
<h2 class="abs section-title" style="top:2444px;color:#fff">OUR SERVICES</h2>

<div class="abs service" style="left:98px">
  <svg width="50" height="44" viewBox="0 0 50 44"><rect x="2" y="2" width="46" height="30" rx="3" fill="#fff"/><rect x="6" y="6" width="38" height="22" fill="#234f8e"/><rect x="20" y="32" width="10" height="6" fill="#fff"/><rect x="13" y="38" width="24" height="4" rx="1" fill="#fff"/></svg>
  <h4>PORRO QUISQUAM</h4>
  <p>It has survived not only five centuries, but also the leap into electronic typesetting, remaining essentially unchanged.</p>
</div>
<div class="abs service" style="left:435px">
  <svg width="56" height="44" viewBox="0 0 56 44"><g fill="#fff" stroke="#234f8e" stroke-width="2"><path d="M28 2l12 6-12 6-12-6z"/><path d="M16 8l12 6v14l-12-6z"/><path d="M40 8l-12 6v14l12-6z"/><path d="M14 22l12 6-12 6-12-6z"/><path d="M2 28l12 6v10L2 38z"/><path d="M26 28l-12 6v10l12-6z"/><path d="M42 22l12 6-12 6-12-6z"/><path d="M30 28l12 6v10l-12-6z"/><path d="M54 28l-12 6v10l12-6z"/></g></svg>
  <h4>DOLOREM IPSUM</h4>
  <p>It has survived not only five centuries, but also the leap into electronic typesetting, remaining essentially unchanged.</p>
</div>
<div class="abs service" style="left:768px">
  <svg width="50" height="44" viewBox="0 0 50 44"><path d="M48 2L2 22l14 5 3 15 8-10 12 9z" fill="#fff"/><path d="M16 27L48 2 22 30" fill="none" stroke="#234f8e" stroke-width="2"/></svg>
  <h4>CONSECTETUR</h4>
  <p>It has survived not only five centuries, but also the leap into electronic typesetting, remaining essentially unchanged.</p>
</div>

<h2 class="abs section-title" style="top:2940px">CONTACT US</h2>
<div class="abs contact-field" style="left:186px;top:3016px;width:367px">Name</div>
<div class="abs contact-field" style="left:624px;top:3016px;width:365px">Email id</div>
<div class="abs contact-field" style="left:186px;top:3068px;width:803px">Message</div>
<div class="abs submit">SUBMIT</div>

<footer class="abs footer">
  <nav class="abs footer-links">ABOUT &nbsp;|&nbsp; PRIVACY &nbsp;|&nbsp; TERMS &nbsp;|&nbsp; LEGAL &nbsp;|&nbsp; CONTACT</nav>
  <div class="abs footer-social"><span></span><span></span><span></span><span></span><span></span><span></span></div>
  <p class="abs copyright">Copyright © 2017 &nbsp;All Rights Reserved</p>
</footer>

</body>
</html>
```